Business card design for Plumbing and Gas fitting company

We need a business card design for our plumbing and gas fitting company using the company logo and director details. Design should be modern and eye-catching however kept reasonably simple. This design should be targeted at commercial businesses/work so professionalism is key.

Target Market(s)

Commercial/business

Industry/Entity Type

Plumbing

Contact Information for Business Card

Warren Dohey
Director
027 581 9043
warren@vantorplumbingandgas.example
PO Box 7816
Palmerston North 4472

Font styles to use
Sans Serif

Requirements
Must have
• Logo
• Modern
• Kept simple
Nice to have
• Colour scheme based around logo

```html
<!DOCTYPE html>
<html lang="en">
<head>
<meta charset="utf-8">
<title>Vantor Plumbing &amp; Gas – Business Card</title>
<link rel="stylesheet" href="https://fonts.googleapis.com/css2?family=Open+Sans:wght@400;600;700&display=swap">
<style>
  :root {
    --backdrop: #2b2b2d;
    --card-white: #ffffff;
    --brand-blue: #1f7dc4;
    --brand-orange: #e67a32;
    --text-grey: #6f6f72;
    --rule-grey: #b9b9bd;
    --white: #ffffff;
  }
  * { box-sizing: border-box; margin: 0; padding: 0; }
  html, body {
    width: 1200px; height: 950px; overflow: hidden;
    background: var(--backdrop);
    font-family: "Open Sans", Arial, sans-serif;
  }
  .card {
    position: absolute;
    left: 280px;
    width: 640px; height: 391px;
    border-radius: 4px;
    overflow: hidden;
  }
  .card--front { top: 60px; background: var(--card-white); }
  .card--back { top: 499px; background: var(--brand-orange); }

  /* front */
  .front-edge {
    position: absolute; left: 0; right: 0; bottom: 0; height: 14px;
    background: var(--brand-blue);
    border-top: 5px solid var(--brand-orange);
  }
  .brand {
    display: flex; align-items: center; gap: 12px;
  }
  .brand__dot {
    width: 30px; height: 30px; border-radius: 50%;
    flex: none;
  }
  .brand__name { font-weight: 700; white-space: nowrap; }
  .card--front .brand {
    position: absolute; right: 46px; top: 58px;
  }
  .card--front .brand__dot { background: var(--brand-blue); }
  .card--front .brand__name { color: var(--brand-blue); font-size: 28px; }

  .front-rule {
    position: absolute; left: 46px; right: 46px; top: 160px;
    height: 1px; background: var(--rule-grey);
  }
  .person {
    position: absolute; left: 46px; top: 186px;
  }
  .person__name { color: var(--brand-blue); font-size: 22px; font-weight: 600; line-height: 1.2; }
  .person__role { color: var(--brand-orange); font-size: 15px; line-height: 1.3; }

  .contacts {
    position: absolute; left: 46px; top: 268px;
    list-style: none;
  }
  .contacts li {
    display: flex; align-items: center; gap: 9px;
    color: var(--text-grey); font-size: 14px; line-height: 24px;
  }
  .contacts svg { width: 15px; height: 15px; flex: none; }

  .address {
    position: absolute; right: 46px; top: 186px;
    text-align: right;
    color: var(--text-grey); font-size: 15px; line-height: 1.45;
  }

  /* back */
  .card--back .brand {
    position: absolute; left: 50%; top: 150px; transform: translateX(-50%);
  }
  .card--back .brand__dot { background: var(--white); }
  .card--back .brand__name { color: var(--white); font-size: 36px; }
  .web {
    position: absolute; left: 0; right: 0; top: 240px;
    text-align: center; color: var(--white);
    font-size: 15px; letter-spacing: 1px;
  }
</style>
</head>
<body>

<section class="card card--front" aria-label="Business card front">
  <div class="brand">
    <span class="brand__dot"></span>
    <span class="brand__name">Vantor Plumbing &amp; Gas</span>
  </div>

  <div class="front-rule"></div>

  <div class="person">
    <p class="person__name">Warren Dohey</p>
    <p class="person__role">Director</p>
  </div>

  <div class="address">
    <p>PO Box 7816</p>
    <p>Palmerston North 4472</p>
  </div>

  <ul class="contacts">
    <li>
      <svg viewBox="0 0 16 16" aria-hidden="true"><rect width="16" height="16" rx="3" fill="#1f7dc4"/><path d="M5 3.5l1.6 0 .8 2.3-1.1.9c.5 1.2 1.3 2 2.5 2.5l.9-1.1 2.3.8v1.6c0 .6-.5 1-1.1 1C6.9 11.3 4.7 9.1 4 5.6 4 4 4.4 3.5 5 3.5z" fill="#fff"/></svg>
      <span>027 581 9043</span>
    </li>
    <li>
      <svg viewBox="0 0 16 16" aria-hidden="true"><rect width="16" height="16" rx="3" fill="#1f7dc4"/><rect x="3" y="4.5" width="10" height="7" fill="none" stroke="#fff" stroke-width="1.2"/><path d="M3 4.5l5 4 5-4" fill="none" stroke="#fff" stroke-width="1.2"/></svg>
      <span>warren@vantorplumbingandgas.example</span>
    </li>
    <li>
      <svg viewBox="0 0 16 16" aria-hidden="true"><circle cx="8" cy="8" r="8" fill="#1f7dc4"/><circle cx="8" cy="8" r="4.6" fill="none" stroke="#fff" stroke-width="1.1"/><path d="M3.4 8h9.2M8 3.4c-2 2.6-2 6.6 0 9.2M8 3.4c2 2.6 2 6.6 0 9.2" fill="none" stroke="#fff" stroke-width="1"/></svg>
      <span>vantorplumbingandgas.example</span>
    </li>
  </ul>

  <div class="front-edge"></div>
</section>

<section class="card card--back" aria-label="Business card back">
  <div class="brand">
    <span class="brand__dot"></span>
    <span class="brand__name">Vantor Plumbing &amp; Gas</span>
  </div>
  <p class="web">www.vantorplumbingandgas.example</p>
</section>

</body>
</html>
```